Two (Similar) Posters - Both 11" x 17"

We are looking for two posters - both 11" x 17" (vertical orientation) - to promote two consecutive, cardiology-related events:

Poster #1) The Inaugural New York RMC Quizline Competition, Cocktail Reception and Whiskey Tasting (http://brelvan-hsq.org/quizline-and-reception)

and

Poster #2) The 89th Annual Scientific Session and 27th Annual Meeting (http://brelvan-hsq.org/2017annualmtg)

#1 is a cocktail party with a whiskey tasting that will also feature a gameshow-like event with the med students, and #2 is an educational conference for doctors

Target Market(s)

Healthcare providers (Please do not include stock images of medical professionals; in fact, please use caution with any stock imagery, as it most likely will not be appropriate.)

Industry/Entity Type

Education

Colors

Designer to choose colors to be used in the design.

Requirements
Must have
• Each poster design should include:
• - the 4 logos of the participating organizations (I can upload various other versions if needed) along with the "wording" that goes alongside each one (see "STD_small" image as an example)
• - name of event
• - date, time and location
• - where to register
• - where to get more information
• - some artistic flavor or detailing
• Final (raw) files in an .ai, .psd, .eps or .idml format are required upon project completion.
Nice to have
• It's not crucial that these two posters "match," but it would be nice if they at least coordinated with each other. Would be nice if the designer could stay close to our color scheme (can be found here - http://brelvan-hsq.org/), but this isn't crucial. Posters should be upscale, neat and professional.
Should not have
• Should not be too difficult to read. These are posters that will likely be hanging on a bulletin board in hospital staff break rooms. Should not be too cartoon-like or silly. The two should not look EXACTLY the same in case people think that they are the same poster.

```html
<!DOCTYPE html>
<html lang="en">
<head>
<meta charset="utf-8">
<title>The Inaugural New York RMC Quizline Competition</title>
<link rel="stylesheet" href="https://fonts.googleapis.com/css2?family=EB+Garamond:wght@400;500&family=Roboto+Condensed:wght@500;700&display=swap">
<style>
  :root {
    --navy: #1b3057;
    --steel: #234d72;
    --tan: #aba683;
    --ink: #1e1e1e;
    --grey: #555;
    --rule: #9a9a9a;
    --white: #ffffff;
  }
  * { box-sizing: border-box; margin: 0; padding: 0; }
  html, body { width: 776px; height: 1200px; overflow: hidden; background: var(--white); }
  .poster { position: relative; width: 776px; height: 1200px; font-family: "EB Garamond", Georgia, serif; color: var(--ink); overflow: hidden; }

  .top-bar { position: absolute; left: 0; top: 0; width: 776px; height: 27px; background: var(--navy); }
  .top-stripe { position: absolute; left: 0; top: 27px; width: 776px; height: 12px; background: var(--tan); }
  .hero { position: absolute; left: 0; top: 39px; width: 776px; height: 268px;
    background: linear-gradient(100deg, #8a8f86 0%, #5c574c 35%, #3f3b34 55%, #6d7478 80%, #3a4046 100%); }

  .ribbon { position: absolute; left: 332px; top: 0; width: 112px; height: 240px; }
  .ribbon-label { position: absolute; left: 332px; top: 0; width: 112px; text-align: center; }
  .ribbon-mark { width: 58px; height: 58px; border-radius: 50%; background: var(--navy); margin: 28px auto 10px; }
  .ribbon-name { font-size: 17px; line-height: 1.05; color: var(--navy); font-weight: 400; }

  .badge { position: absolute; left: 353px; top: 272px; width: 70px; height: 70px; border-radius: 50%;
    background: var(--tan); border: 3px solid var(--white); display: flex; align-items: center; justify-content: center; }

  .title { position: absolute; left: 0; top: 380px; width: 776px; text-align: center; font-weight: 400;
    font-size: 47px; line-height: 71px; letter-spacing: -0.3px; }

  .details { position: absolute; left: 0; top: 616px; width: 776px; display: flex; justify-content: space-around; padding: 0 30px; }
  .detail { width: 230px; text-align: center; font-size: 19.5px; line-height: 26px; color: #333; }
  .detail-icon { width: 72px; height: 72px; border-radius: 50%; border: 1px solid var(--rule); margin: 0 auto 26px;
    display: flex; align-items: center; justify-content: center; }

  .band { position: absolute; left: 0; width: 776px; display: flex; align-items: center; color: var(--white); }
  .band-register { top: 833px; height: 120px; background: var(--tan); }
  .band-info { top: 953px; height: 120px; background: var(--steel); }
  .band-icon { width: 258px; display: flex; justify-content: center; }
  .band-icon span { width: 58px; height: 58px; border-radius: 50%; border: 1.5px solid var(--white);
    display: flex; align-items: center; justify-content: center; }
  .band-divider { width: 1px; height: 86px; background: rgba(255,255,255,0.7); margin-right: 82px; }
  .band-register .band-text { color: #1e1e1e; font-size: 21px; line-height: 26px; }
  .band-info .band-text { font-size: 17px; line-height: 21px; }
  .strong { font-family: "Roboto Condensed", Arial, sans-serif; font-weight: 500; }
  .band-register .strong { font-size: 20px; color: var(--navy); }
  .band-info .strong { font-size: 16px; font-weight: 700; }

  .partners-label { position: absolute; left: 0; top: 1080px; width: 776px; text-align: center; font-size: 14px; color: var(--grey); }
  .partners { position: absolute; left: 0; top: 1112px; width: 776px; display: flex; justify-content: space-around; padding: 0 70px; }
  .partner { width: 58px; height: 58px; border-radius: 50%; background: var(--navy); }
  .partner.light { background: #c9cbd2; }
  .bottom-bar { position: absolute; left: 0; top: 1185px; width: 776px; height: 15px; background: var(--navy); }
</style>
</head>
<body>
<main class="poster">
  <div class="top-bar"></div>
  <div class="top-stripe"></div>
  <div class="hero" role="img" aria-label="Photograph of a wooden desk with paperwork, reading glasses, a calculator and a hand filling in a form with a pen"></div>

  <svg class="ribbon" viewBox="0 0 112 240" aria-hidden="true">
    <polygon points="0,0 112,0 112,240 56,206 0,240" fill="#4a4a45" opacity="0.5"/>
    <polygon points="0,0 112,0 112,236 56,202 0,236" fill="#ffffff"/>
  </svg>
  <div class="ribbon-label">
    <div class="ribbon-mark"></div>
    <div class="ribbon-name">Brelvan Heart Society</div>
  </div>

  <div class="badge">
    <svg width="26" height="26" viewBox="0 0 26 26" aria-hidden="true">
      <path d="M2 3h22l-9 11v7h5v2H6v-2h5v-7z" fill="#fff"/>
    </svg>
  </div>

  <h1 class="title">The Inaugural<br>New York RMC Quizline Competition,<br>Cocktail Reception &amp; Whiskey Tasting</h1>

  <section class="details">
    <div class="detail">
      <div class="detail-icon">
        <svg width="24" height="24" viewBox="0 0 24 24" aria-hidden="true"><circle cx="12" cy="12" r="11" fill="#777"/><path d="M12 5v7h5" stroke="#fff" stroke-width="2" fill="none"/></svg>
      </div>
      Wednesday,<br>Dec. 6th, 2017,<br>from 6:30 p.m.<br>to 10:30 p.m.
    </div>
    <div class="detail">
      <div class="detail-icon">
        <svg width="20" height="26" viewBox="0 0 20 26" aria-hidden="true"><path d="M10 1a9 9 0 0 0-9 9c0 7 9 15 9 15s9-8 9-15a9 9 0 0 0-9-9z" fill="#777"/><circle cx="10" cy="10" r="3.5" fill="#fff"/></svg>
      </div>
      Oak &amp; Ember,<br>14 E 52nd St,<br>New York,<br>NY 10022
    </div>
    <div class="detail">
      <div class="detail-icon">
        <svg width="24" height="24" viewBox="0 0 24 24" aria-hidden="true"><circle cx="12" cy="12" r="11" fill="#777"/><text x="12" y="17" text-anchor="middle" font-family="Arial, sans-serif" font-size="14" font-weight="700" fill="#fff">$</text></svg>
      </div>
      Free for<br>BHS/HSQ Members<br>and $30<br>for nonmembers &amp; guests
    </div>
  </section>

  <section class="band band-register">
    <div class="band-icon"><span>
      <svg width="20" height="18" viewBox="0 0 20 18" aria-hidden="true"><path d="M10 17S1 11 1 5.5A4.5 4.5 0 0 1 10 3.5 4.5 4.5 0 0 1 19 5.5C19 11 10 17 10 17z" fill="#fff"/></svg>
    </span></div>
    <div class="band-divider"></div>
    <p class="band-text">Register online at<br><span class="strong">www.brelvan-hsq.org/2017annualmtg</span></p>
  </section>

  <section class="band band-info">
    <div class="band-icon"><span>
      <svg width="10" height="22" viewBox="0 0 10 22" aria-hidden="true"><circle cx="5" cy="3" r="2.5" fill="#fff"/><path d="M2 8h5v11h2v2H1v-2h2v-9H2z" fill="#fff"/></svg>
    </span></div>
    <div class="band-divider"></div>
    <p class="band-text">For more information<br>or to inquire about becoming an exhibitor,<br><span class="strong">call (212) 555-0147 or email ask@brelvan-hsq.org</span></p>
  </section>

  <p class="partners-label">With the assistance of:</p>
  <div class="partners">
    <div class="partner"></div>
    <div class="partner"></div>
    <div class="partner light"></div>
    <div class="partner light"></div>
  </div>

  <div class="bottom-bar"></div>
</main>
</body>
</html>
```